Logo Call Center Consultants
Red Otter Consultants
Project: Logo Call Center Consultants
Logo Call Center Consultants - Consulting
Creative Brief
Bright & Fun-filled
Corin Maltby
President
317 Juniper Crescent Box 82 Larchmere Cove, BC V0P 2K4
877.XXX.XXXX
cmaltby@redotterconsulting.example
redotterconsulting.example

```html
<!DOCTYPE html>
<html lang="en">
<head>
<meta charset="utf-8">
<title>Red Otter Consultants – Business Card</title>
<link href="https://fonts.googleapis.com/css2?family=Questrial&display=swap" rel="stylesheet">
<style>
  :root {
    --backdrop-light: #a3a3a3;
    --backdrop-dark: #6f6f6f;
    --card-white: #f4f6f8;
    --brand-blue: #1b86d4;
    --deep-blue: #0b5fae;
    --sky-blue: #4fb2ee;
    --ink-grey: #8a9199;
    --paper-white: #ffffff;
  }
  * { box-sizing: border-box; margin: 0; padding: 0; }
  html, body {
    width: 1200px;
    height: 838px;
    overflow: hidden;
  }
  body {
    background: radial-gradient(ellipse at 50% 40%, var(--backdrop-light), var(--backdrop-dark));
    font-family: "Questrial", "Century Gothic", sans-serif;
    position: relative;
  }
  .card {
    position: absolute;
    top: 270px;
    width: 520px;
    height: 297px;
    border-radius: 4px;
    box-shadow: 0 18px 40px rgba(0,0,0,0.28);
    overflow: hidden;
  }
  .card-front {
    left: 50px;
    background: var(--card-white);
  }
  .card-back {
    left: 630px;
    background: var(--deep-blue);
  }
  .brand {
    position: absolute;
    left: 40px;
    top: 46px;
    display: flex;
    align-items: center;
    gap: 12px;
  }
  .brand-mark {
    width: 30px;
    height: 30px;
    background: var(--brand-blue);
  }
  .brand-name {
    color: var(--brand-blue);
    font-size: 30px;
    letter-spacing: 0.5px;
  }
  .person {
    position: absolute;
    left: 40px;
    bottom: 52px;
  }
  .person-name {
    color: var(--brand-blue);
    font-size: 24px;
  }
  .person-title {
    color: var(--ink-grey);
    font-size: 14px;
    margin-top: 4px;
  }
  .facets {
    position: absolute;
    inset: 0;
  }
  .contact-list {
    position: absolute;
    right: 30px;
    top: 84px;
    list-style: none;
    color: var(--paper-white);
    font-size: 14px;
    text-align: right;
  }
  .contact-list li {
    display: flex;
    align-items: center;
    justify-content: flex-end;
    gap: 8px;
    margin-bottom: 8px;
  }
  .contact-email {
    position: absolute;
    left: 30px;
    top: 84px;
    display: flex;
    align-items: center;
    gap: 8px;
    color: var(--paper-white);
    font-size: 14px;
  }
  .website {
    position: absolute;
    right: 30px;
    bottom: 34px;
    color: var(--paper-white);
    font-size: 15px;
  }
  .icon { width: 13px; height: 13px; flex: none; }
</style>
</head>
<body>

  <section class="card card-front" aria-label="Business card front">
    <div class="brand">
      <span class="brand-mark"></span>
      <span class="brand-name">Red Otter Consultants</span>
    </div>
    <div class="person">
      <p class="person-name">Corin Maltby</p>
      <p class="person-title">President</p>
    </div>
  </section>

  <section class="card card-back" aria-label="Business card back">
    <svg class="facets" viewBox="0 0 520 297" preserveAspectRatio="none">
      <defs>
        <linearGradient id="facet-light" x1="0" y1="0" x2="1" y2="1">
          <stop offset="0" stop-color="#4fb2ee"/>
          <stop offset="1" stop-color="#1b86d4"/>
        </linearGradient>
        <linearGradient id="facet-dark" x1="1" y1="0" x2="0" y2="1">
          <stop offset="0" stop-color="#1b86d4"/>
          <stop offset="1" stop-color="#0b5fae"/>
        </linearGradient>
      </defs>
      <polygon points="0,0 520,0 260,150" fill="url(#facet-light)"/>
      <polygon points="0,0 260,150 0,297" fill="url(#facet-dark)"/>
      <polygon points="520,0 520,297 260,150" fill="#1576c4"/>
      <polygon points="0,297 260,150 520,297" fill="#0d66b6"/>
    </svg>

    <div class="contact-email">
      <svg class="icon" viewBox="0 0 16 16"><rect x="1" y="3" width="14" height="10" rx="1" fill="none" stroke="#fff" stroke-width="1.5"/><polyline points="1,4 8,9 15,4" fill="none" stroke="#fff" stroke-width="1.5"/></svg>
      <span>cmaltby@redotterconsulting.example</span>
    </div>

    <ul class="contact-list">
      <li>
        <svg class="icon" viewBox="0 0 16 16"><path d="M4 1h3l1 4-2 1.5a9 9 0 0 0 3.5 3.5L11 8l4 1v3c0 1-1 2-2 2C7 14 2 9 2 3c0-1 1-2 2-2z" fill="#fff"/></svg>
        <span>877.XXX.XXXX</span>
      </li>
      <li>
        <svg class="icon" viewBox="0 0 16 16"><rect x="4" y="1" width="8" height="14" rx="1.5" fill="#fff"/></svg>
        <span>604.555.0147</span>
      </li>
      <li>
        <svg class="icon" viewBox="0 0 16 16"><rect x="2" y="5" width="12" height="9" rx="1" fill="#fff"/><rect x="4" y="1" width="8" height="4" fill="#fff"/></svg>
        <span>925.555.0163</span>
      </li>
    </ul>

    <p class="website">www.redotterconsulting.example</p>
  </section>

</body>
</html>
```